Kestrel Arc Services business card Design

I need a business card that will wow clients at first sight.

Kestrel Arc Services connects people with HOME & LIFESTYLE SERVICES, and the client pays the value that was created by our service, using. 'Settle On The Sum That Feels Fair".
Please look us up at www.kestrelarcservices.example to see our mission and services.

The new website is being launched in 8 weeks.

I need a business card to campaign LANDSCAPING however please design it to be easily modified to CLEANING SERVICE, PLUMBING Etc Etc.

Until our SEO campaign begins working I need business cards to leave with prospective clients for each individual service as appropriate.

Dorian Maltby
Creative Director
www.kestrelarcservices.example
1-888-517-4KAS
email: info@kestrelarcservices.example

Target Market(s)

Residential and commercial clients

Industry/Entity Type

Business

Contact Information for Business Card

2 sided

Font styles to use
Sans Serif

Requirements
Must have
• Im prefering a black card so far
• Logo
• "Settle On The Sum That Feels Fair" seal
• Complete Landscaping & Construction
• Tarnwell Services
• Contact details
• facebook kestrelarc services
• twitter @kestrelarc services
• Adaptable card easily to different services we offer at Kestrel Arc Services as per www.kestrelarcservices.example
Should not have
• Too much imagery

```html
<!DOCTYPE html>
<html lang="en">
<head>
<meta charset="utf-8">
<title>Kestrel Arc Services – Business Card</title>
<link rel="stylesheet" href="https://fonts.googleapis.com/css2?family=Montserrat:wght@300;400;600&family=Open+Sans:wght@400;600;700&display=swap">
<style>
  :root {
    --backdrop: #2b2b2d;
    --card-black: #0d0d0f;
    --brand-blue: #2152a6;
    --brand-blue-light: #4f82d6;
    --card-white: #ffffff;
    --ink: #111111;
    --rule: #1a1a1a;
  }
  * { box-sizing: border-box; margin: 0; padding: 0; }
  html, body {
    width: 1200px; height: 900px; overflow: hidden;
    background: var(--backdrop);
  }
  .stage {
    width: 1200px; height: 900px;
    display: flex; flex-direction: column; align-items: center; justify-content: center;
    gap: 44px;
  }
  .card {
    position: relative;
    width: 640px; height: 366px;
    border-radius: 22px;
    overflow: hidden;
  }

  /* Brand block */
  .brand { position: absolute; display: flex; align-items: center; gap: 14px; }
  .brand-mark { width: 46px; height: 46px; border-radius: 50%; flex: none; }
  .brand-text { display: flex; flex-direction: column; }
  .brand-name {
    font-family: "Montserrat", sans-serif; font-weight: 400;
    font-size: 30px; line-height: 1; letter-spacing: -0.3px; white-space: nowrap;
  }
  .brand-suffix { font-size: 15px; margin-left: 4px; }
  .brand-tagline {
    font-family: "Montserrat", sans-serif; font-weight: 400;
    font-size: 8.5px; letter-spacing: 3px; text-transform: uppercase; margin-top: 6px;
    white-space: nowrap;
  }

  /* Front */
  .card-front { background: var(--card-black); color: var(--card-white); }
  .card-front .brand { left: 34px; bottom: 48px; }
  .card-front .brand-mark { background: var(--card-white); }
  .card-front .brand-tagline { color: var(--brand-blue-light); }

  .seal {
    position: absolute; right: 34px; top: 34px;
    width: 104px; height: 104px; border-radius: 50%;
    border: 2px solid var(--brand-blue-light);
    display: flex; align-items: center; justify-content: center; text-align: center;
    padding: 14px;
    font-family: "Montserrat", sans-serif; font-weight: 600;
    font-size: 10px; line-height: 1.3; text-transform: uppercase; letter-spacing: 0.3px;
    color: var(--card-white);
  }
  .social {
    position: absolute; right: 34px; top: 172px;
    list-style: none;
    font-family: "Open Sans", sans-serif; font-size: 14px;
    display: flex; flex-direction: column; gap: 8px;
  }
  .social li { display: flex; align-items: center; gap: 8px; }
  .social-chip { width: 13px; height: 13px; background: var(--card-white); border-radius: 2px; }

  /* Back */
  .card-back { background: var(--card-white); color: var(--ink); }
  .card-back .brand { left: 30px; top: 56px; }
  .card-back .brand-mark { background: var(--brand-blue); }
  .card-back .brand-tagline { color: var(--brand-blue); }
  .person {
    position: absolute; right: 30px; top: 150px; text-align: right;
    font-family: "Open Sans", sans-serif;
  }
  .person-name { font-weight: 700; font-size: 23px; text-transform: uppercase; letter-spacing: 0.2px; line-height: 1.1; }
  .person-role { font-weight: 400; font-size: 14px; color: var(--brand-blue); text-transform: uppercase; }
  .contact-list { list-style: none; margin-top: 12px; font-size: 13.5px; line-height: 1.45; }
  .contact-list li { display: flex; align-items: center; justify-content: flex-end; gap: 8px; }
  .contact-icon { width: 12px; height: 12px; flex: none; }
  .rule-h { position: absolute; left: 150px; right: 240px; top: 196px; height: 1.5px; background: var(--rule); }
  .rule-v { position: absolute; left: 150px; top: 196px; bottom: 0; width: 1.5px; background: var(--rule); }
  .service-line {
    position: absolute; right: 30px; bottom: 28px;
    font-family: "Open Sans", sans-serif; font-weight: 600;
    font-size: 13px; letter-spacing: 1.5px; text-transform: uppercase;
    color: var(--brand-blue);
  }
</style>
</head>
<body>
<main class="stage">

  <section class="card card-front" aria-label="Card front">
    <p class="seal">&ldquo;Settle On The Sum That Feels Fair&rdquo;</p>
    <ul class="social">
      <li><span class="social-chip"></span>kestrelarc services</li>
      <li><span class="social-chip"></span>@kestrelarc services</li>
    </ul>
    <div class="brand">
      <span class="brand-mark"></span>
      <div class="brand-text">
        <span class="brand-name">Kestrel Arc Services<span class="brand-suffix">Inc.</span></span>
        <span class="brand-tagline">Complete Landscaping &amp; Construction</span>
      </div>
    </div>
  </section>

  <section class="card card-back" aria-label="Card back">
    <div class="brand">
      <span class="brand-mark"></span>
      <div class="brand-text">
        <span class="brand-name">Kestrel Arc Services<span class="brand-suffix">Inc.</span></span>
        <span class="brand-tagline">Complete Landscaping &amp; Construction</span>
      </div>
    </div>

    <div class="rule-h"></div>
    <div class="rule-v"></div>

    <div class="person">
      <p class="person-name">Dorian Maltby</p>
      <p class="person-role">Creative Director</p>
      <ul class="contact-list">
        <li>1-888-517-4KAS
          <svg class="contact-icon" viewBox="0 0 12 12" aria-hidden="true"><path d="M2.5 1 L4.5 1 L5.2 3.6 L4 4.6 Q5.2 7 7.4 8 L8.4 6.8 L11 7.5 L11 9.5 Q10.5 11 9 11 Q1 10 1 2.8 Q1 1.2 2.5 1 Z" fill="var(--brand-blue)"/></svg>
        </li>
        <li>info@kestrelarcservices.example
          <svg class="contact-icon" viewBox="0 0 12 12" aria-hidden="true"><rect x="0.8" y="2.3" width="10.4" height="7.4" rx="1" fill="none" stroke="var(--brand-blue)" stroke-width="1.2"/><path d="M1 2.8 L6 6.6 L11 2.8" fill="none" stroke="var(--brand-blue)" stroke-width="1.2"/></svg>
        </li>
        <li>www.kestrelarcservices.example
          <svg class="contact-icon" viewBox="0 0 12 12" aria-hidden="true"><g fill="none" stroke="var(--brand-blue)" stroke-width="1.1"><circle cx="6" cy="6" r="5"/><ellipse cx="6" cy="6" rx="2.2" ry="5"/><path d="M1 6 H11"/></g></svg>
        </li>
      </ul>
    </div>

    <p class="service-line">Tarnwell Services</p>
  </section>

</main>
</body>
</html>
```